Female Vocalist Needs Design for Music Album

Hi, my name is Corinna Vashti and I need a design for my first album. It will be a Digipak, 4 panel (1tray) and disk. (I will be using pressforge to print the CDs. Please see http://www.pressforgeworks.example/templates/ for digipak template and design specs.)
The musical genre of this album is sacred/religious/gospel- solo mezzo soprano with solo piano accompaniment. The musical style is traditional with a few pieces that have a more contemporary feel.
I would like to see designs that have the following:
FRONT COVER (Panel 1):
Photo of the artist, name of the artist, and album title: Lift Up Your Lantern (see attached). Try to create the feeling that the artist is alone in the shadows and light from heaven is pouring down onto her face as she is crying out to God. Font for the artist name in a flowing script-like calligraphic handwriting.
BACK COVER (Panel 2):
Photo of the artist and the track list (see attached).
INSIDE PANEL (Panel 3 - Back side of Front Cover):
Dedication, Special Thank You, and Credits (see attached). May include a picture of the recording artist.
CD TRAY PANEL (Panel 4):
Background using the design elements and colors used throughout, but no photos of the artist.
CD DISK DESIGN:
Name of the artist and album title on background using design elements and colors used throughout, but no photos of the artist.
I would like to see some 'sophistication' (for lack of a better word) in the design. It may be elegantly simple, or more elaborate- something well thought out down to the choice of font style and placement. Please feel free to use your imagination and creativity. The final design should enhance the photo of the artist and go with the overall prayerful theme of the album title.
Attached are some design examples that I found interesting.
Updates
For those who did not get the album text, I just re posted the attachment. I apologize...I thought I had attached it, but apparently accidentally detached it when I was editing the brief. We added the track lengths and made a few corrections and additions to the album text. Please see the attached Word Document "Corinna Vashti Album Text" on the brief. Thank you.
Target Market(s)
Target market are Christians and people of faith.
Industry/Entity Type
Religious
Requirements
Must have
- For the front cover, please use photo P1140955. For the back cover, please use photo P1140515.
Nice to have
- Retouch the artist photo to remove any incidental blemishes. Remove any distracting elements like in the photo backgrounds, unless you think it goes with the design theme. Crop photos as necessary. Please use your best judgement on whether to keep the photo background or to enhance it, add on to it, or completely change the backgrounds and/or to add other design elements and ornamentation. If another background is used, make sure it does not clash with what the artist is wearing and there is still good contrast between the photo and the background. One idea could be to use a off-white/light grey background on the outside covers and red on the inside covers. Ornamentation should be light, translucent, and subtle.
Should not have
- The design should NOT include any religious symbols or icons such as crosses, fishes, doves, etc., and no cartoon-like clip art.

```html
<!DOCTYPE html>
<html lang="en">
<head>
<meta charset="utf-8">
<title>Corinna Vashti – Lift Up Your Lantern – Disc Print</title>
<link rel="stylesheet" href="https://fonts.googleapis.com/css2?family=Pinyon+Script&family=Cormorant+Garamond:wght@500&family=PT+Sans:wght@400;700&display=swap">
<style>
  :root {
    --paper: #ffffff;
    --ink: #111111;
    --disc-red: #e61f33;
    --coral: #ea6a5a;
    --coral-deep: #de6352;
    --title-white: #ffffff;
    --tag-grey: #555555;
  }
  html, body {
    margin: 0;
    padding: 0;
    overflow: hidden;
    background: var(--paper);
  }
  .template-sheet {
    position: relative;
    width: 1200px;
    height: 1200px;
    background: var(--paper);
    color: var(--ink);
    font-family: "PT Sans", Arial, sans-serif;
    overflow: hidden;
  }
  .template-tag {
    position: absolute;
    left: 32px;
    top: 30px;
    display: flex;
    align-items: flex-start;
    gap: 8px;
  }
  .template-tag__square {
    width: 48px;
    height: 60px;
    background: var(--tag-grey);
    border-radius: 6px;
  }
  .template-tag__info {
    display: flex;
    flex-direction: column;
    align-items: center;
    line-height: 1.05;
    font-weight: 700;
  }
  .template-tag__code { font-size: 24px; }
  .template-tag__line { font-size: 11px; }
  .template-tag__small { font-size: 8px; }
  .template-tag__paste {
    position: absolute;
    left: 36px;
    top: 104px;
    font-size: 12px;
  }
  .print-log {
    position: absolute;
    left: 914px;
    top: 10px;
    font-size: 14px;
    line-height: 14.5px;
  }
  .disc-art {
    position: absolute;
    left: 0;
    top: 0;
  }
  .disc-artist {
    font-family: "Pinyon Script", cursive;
    font-size: 58px;
    fill: var(--title-white);
  }
  .disc-title {
    font-family: "Cormorant Garamond", Georgia, serif;
    font-weight: 500;
    font-size: 47px;
    fill: var(--title-white);
  }
  .notes-label {
    position: absolute;
    left: 38px;
    top: 1034px;
    font-size: 24px;
  }
</style>
</head>
<body>
<main class="template-sheet">
  <header class="template-tag">
    <div class="template-tag__square"></div>
    <div class="template-tag__info">
      <span class="template-tag__code">UD109</span>
      <span class="template-tag__line">pressforge</span>
      <span class="template-tag__line">On Disc Print</span>
      <span class="template-tag__small">Vector Studio</span>
      <span class="template-tag__small">01/17/12 mk</span>
    </div>
  </header>
  <div class="template-tag__paste">PASTE OFA TAG HERE</div>

  <div class="print-log">
    COLOR:<br>PRINTS: 1 of 3<br>
    COLOR:<br>PRINTS: 2 of 3<br>
    COLOR:<br>PRINTS: 3 of 3
  </div>

  <svg class="disc-art" width="1200" height="1200" viewBox="0 0 1200 1200" aria-label="Disc face">
    <defs>
      <clipPath id="disc-clip">
        <circle cx="596" cy="602" r="402"/>
      </clipPath>
      <radialGradient id="ornament-glow" cx="0.52" cy="0.42" r="0.62">
        <stop offset="0" stop-color="var(--coral-deep)"/>
        <stop offset="0.45" stop-color="var(--coral)" stop-opacity="0.85"/>
        <stop offset="1" stop-color="var(--disc-red)" stop-opacity="0"/>
      </radialGradient>
      <filter id="title-shadow" x="-10%" y="-30%" width="120%" height="160%">
        <feDropShadow dx="1.5" dy="1.5" stdDeviation="1.2" flood-color="#5a0a12" flood-opacity="0.55"/>
      </filter>
    </defs>

    <circle class="disc-face" cx="596" cy="602" r="402" fill="var(--disc-red)"/>

    <rect class="disc-ornament" x="194" y="200" width="804" height="804"
          clip-path="url(#disc-clip)" fill="url(#ornament-glow)"
          role="img" aria-label="Coral paint splatter ornament over a swirling line motif"/>

    <g class="disc-titles" filter="url(#title-shadow)">
      <text class="disc-artist" x="650" y="776" text-anchor="middle">Corinna Vashti</text>
      <text class="disc-title" x="606" y="832" text-anchor="middle">LIFT UP YOUR LANTERN</text>
    </g>
  </svg>

  <div class="notes-label">Notes:</div>
</main>
</body>
</html>
```